Kit Layout de Posts para Redes Sociais (Facebook, Instagram e etc)para Dra Marcela Toledano
Postado por: marcelatoledano_5830174416   Estou Offline
Projeto para criar:
Kit Layout de Posts para Redes Sociais (Facebook, Instagram e etc)
Clientes com PC preferem arquivos em CorelDraw (CDR).
Imagem: Imagem JPG (alta resoluçao) PNG em camadas PSD em camadas PDF Sem Preferência Tipos possíveis: Imagem JPG (alta resoluçao), PNG em camadas, PSD em camadas, PDF.

```html
<!DOCTYPE html>
<html lang="pt-BR">
<head>
<meta charset="utf-8">
<title>Post – Dra. Marcela Toledano</title>
<link href="https://fonts.googleapis.com/css2?family=Oswald:wght@500;600&family=Great+Vibes&display=swap" rel="stylesheet">
<style>
  :root {
    --bg: #e8e5e2;
    --mauve: #8a6a82;
    --skin: #d9b39c;
    --skin-light: #ead3c4;
    --glove: #f5f5f5;
  }
  html, body {
    margin: 0;
    padding: 0;
    overflow: hidden;
    background: var(--bg);
  }
  .post {
    position: relative;
    width: 1200px;
    height: 1200px;
    overflow: hidden;
    background: var(--bg);
  }
  .photo {
    position: absolute;
    left: 360px;
    top: 240px;
    width: 840px;
    height: 960px;
    border-radius: 420px 420px 0 0;
    background:
      linear-gradient(90deg, var(--glove) 0%, var(--glove) 22%, var(--skin-light) 40%, var(--skin) 62%, var(--skin-light) 88%, #e3cbbd 100%);
    z-index: 2;
  }
  .pattern {
    position: absolute;
    background: var(--mauve);
    opacity: 0.85;
  }
  .pattern--left {
    left: 0;
    top: 600px;
    width: 430px;
    height: 250px;
    z-index: 1;
  }
  .pattern--right {
    left: 1100px;
    top: 840px;
    width: 100px;
    height: 170px;
    z-index: 3;
  }
  .headline {
    position: absolute;
    left: 98px;
    top: 48px;
    margin: 0;
    z-index: 4;
    color: var(--mauve);
  }
  .headline__line {
    display: block;
    font-family: "Oswald", sans-serif;
    font-weight: 600;
    font-size: 134px;
    line-height: 148px;
    letter-spacing: -1px;
    text-transform: uppercase;
  }
  .headline__script {
    display: block;
    font-family: "Great Vibes", cursive;
    font-weight: 400;
    font-size: 165px;
    line-height: 160px;
    margin-left: -4px;
  }
  .brand {
    position: absolute;
    left: 890px;
    top: 82px;
    display: flex;
    align-items: center;
    gap: 14px;
    z-index: 4;
    color: var(--mauve);
  }
  .brand__dot {
    width: 60px;
    height: 60px;
    border-radius: 50%;
    border: 4px solid var(--mauve);
    box-sizing: border-box;
    flex: none;
  }
  .brand__text {
    display: flex;
    flex-direction: column;
    font-family: "Oswald", sans-serif;
    font-weight: 500;
    line-height: 1.1;
  }
  .brand__name { font-size: 26px; white-space: nowrap; }
  .brand__tagline {
    font-size: 13px;
    letter-spacing: 3px;
    text-transform: uppercase;
    margin-top: 4px;
  }
</style>
</head>
<body>
<main class="post">
  <h1 class="headline">
    <span class="headline__line">Seu</span>
    <span class="headline__line">Texto</span>
    <span class="headline__script">Aqui</span>
  </h1>

  <div class="brand">
    <span class="brand__dot"></span>
    <span class="brand__text">
      <span class="brand__name">Dra. Marcela Toledano</span>
      <span class="brand__tagline">Cirurgia Plástica</span>
    </span>
  </div>

  <div class="pattern pattern--left" role="img" aria-label="Padrão decorativo de linhas onduladas em lilás"></div>

  <div class="photo" role="img" aria-label="Foto de mulher madura de pele lisa recebendo avaliação facial de mãos com luvas brancas"></div>

  <div class="pattern pattern--right" role="img" aria-label="Padrão decorativo de linhas onduladas em lilás"></div>
</main>
</body>
</html>
```